Eyebrow Tattooist business card design

I am an eyebrow specialist. I wax, shape, tint and tattoo eyebrows. I want a professional but classy image. I like gold raised writing on it. Colour of card either chocolate brown or pale blue??
As I use a technique called feathering and hair strokes, I would like the shape of a eyebrow on the front, with the hair strokes.

Industry/Entity Type
Tattoo
Contact Information for Business Card
I am an eyebrow specialist.
FRONT -  I want the name 'Lush Lids' on the front of the card. With a shape of a brow, with every hair stroke. Need the words 'Tessa brow specialist and cosmetic tattooist' 'using feathered and hairstroke techniques'
03 5162-4730
BACK - At, Serene Glow Spa & Skin Studio. Shop 7, Harlow Grove Plaza, Penfield-Ashbury Road. Penfield East. Vic 3917.
www.lushlids.com.au

```html
<!DOCTYPE html>
<html lang="en">
<head>
<meta charset="utf-8">
<title>Lush Lids – Business Card</title>
<link rel="stylesheet" href="https://fonts.googleapis.com/css2?family=Cormorant+Garamond:wght@600&family=Didact+Gothic&display=swap">
<style>
  :root {
    --page-bg: #f4f2f0;
    --choc-light: #4a2414;
    --choc-mid: #2e140a;
    --choc-dark: #1a0a05;
    --gold-light: #f3dc8c;
    --gold-mid: #c99a36;
    --gold-dark: #8a6418;
    --gold-text: #d9b45a;
    --body-text: #d8cfc8;
  }
  * { margin: 0; padding: 0; box-sizing: border-box; }
  html, body {
    width: 1200px;
    height: 900px;
    overflow: hidden;
    background: var(--page-bg);
  }
  .canvas {
    width: 1200px;
    height: 900px;
    display: flex;
    align-items: center;
    justify-content: center;
    gap: 40px;
  }
  .card {
    position: relative;
    width: 540px;
    height: 320px;
    border-radius: 26px;
    background: var(--choc-dark);
    box-shadow: 0 18px 36px rgba(0, 0, 0, 0.18);
  }
  .card-frame {
    position: absolute;
    inset: 14px;
    border-radius: 18px;
    border: 6px solid transparent;
    background:
      radial-gradient(ellipse at 50% 45%, var(--choc-light) 0%, var(--choc-mid) 55%, var(--choc-dark) 100%) padding-box,
      linear-gradient(135deg, var(--gold-light), var(--gold-mid) 35%, var(--gold-dark) 55%, var(--gold-light) 75%, var(--gold-mid)) border-box;
    display: flex;
    flex-direction: column;
    align-items: center;
    text-align: center;
  }
  .brand-name {
    font-family: "Cormorant Garamond", Georgia, serif;
    font-weight: 600;
    color: var(--gold-text);
    line-height: 1;
  }
  .card-front .brand-name {
    font-size: 74px;
    margin-top: 58px;
  }
  .holder-name {
    font-family: "Cormorant Garamond", Georgia, serif;
    font-weight: 600;
    font-size: 27px;
    color: var(--gold-text);
    margin-top: 26px;
  }
  .services {
    font-family: "Didact Gothic", "Century Gothic", sans-serif;
    font-size: 14.5px;
    line-height: 1.3;
    color: var(--body-text);
    margin-top: 8px;
  }
  .phone {
    font-family: "Didact Gothic", "Century Gothic", sans-serif;
    font-size: 19px;
    color: #f0ebe6;
    margin-top: 2px;
  }
  .card-back .brand-name {
    font-size: 42px;
    margin-top: 44px;
  }
  .address {
    font-style: normal;
    font-family: "Didact Gothic", "Century Gothic", sans-serif;
    font-size: 14px;
    line-height: 1.4;
    color: var(--body-text);
    margin-top: 30px;
  }
  .website {
    font-family: "Didact Gothic", "Century Gothic", sans-serif;
    font-size: 15px;
    color: var(--body-text);
    margin-top: 18px;
  }
</style>
</head>
<body>
  <main class="canvas">
    <section class="card card-front" aria-label="Card front">
      <div class="card-frame">
        <h1 class="brand-name">Lush Lids</h1>
        <p class="holder-name">Tessa brow</p>
        <p class="services">specialist and cosmetic tattooist<br>using feathered and hairstroke techniques</p>
        <p class="phone">03 5162-4730</p>
      </div>
    </section>
    <section class="card card-back" aria-label="Card back">
      <div class="card-frame">
        <h2 class="brand-name">Lush Lids</h2>
        <address class="address">
          At, Serene Glow Spa &amp; Skin Studio.<br>
          Shop 7, Harlow Grove Plaza,<br>
          Penfield-Ashbury Road.<br>
          Penfield East.<br>
          Vic 3917.
        </address>
        <p class="website">www.lushlids.com.au</p>
      </div>
    </section>
  </main>
</body>
</html>
```